Company or website name
- Resume for accounting
- Links to the website
- http://www.gestiondelvallenorte.com/#bienvenidos
- Describe your company and organization and target audience
- The web layout is not for a business. This is a personal site that will present my CV. I am an accountant. It would be nice to follow a model like this website: http://www.gestiondelvallenorte.com/#bienvenidos . The main users of the site will be recruiters.
- The design should have the following
- The design must be modern . There must be both personal photos and scenes work as an office and buildings.

```html
<!DOCTYPE html>
<html lang="en">
<head>
<meta charset="utf-8">
<title>Professional Accountant — CV</title>
<link rel="stylesheet" href="https://fonts.googleapis.com/css2?family=Open+Sans:wght@600;700&family=Tinos:wght@700&family=Carlito:ital,wght@1,400&family=Arimo:wght@700&display=swap">
<style>
  :root {
    --ink: #070707;
    --panel-top: #232323;
    --panel-bottom: #141414;
    --band-blue: #2f4cc8;
    --band-blue-dark: #2139a8;
    --band-blue-light: #4561d8;
    --accent: #8d9ef0;
    --menu-active: #2d3f9c;
    --rule: #3a3a3a;
    --text: #ffffff;
    --text-soft: #eef0fb;
    --icon-grey: #5a5a5a;
    --photo-light: #6b6b6b;
    --photo-dark: #1a1a1a;
  }
  * { margin: 0; padding: 0; box-sizing: border-box; }
  html, body { width: 1200px; height: 991px; overflow: hidden; background: var(--ink); }
  .page { position: relative; width: 1200px; height: 991px; overflow: hidden; background: var(--ink); }
  .shapes { position: absolute; inset: 0; }

  .portrait {
    position: absolute; left: 705px; top: 52px; width: 365px; height: 520px;
    background: radial-gradient(ellipse at 50% 45%, var(--photo-light) 0%, #3c3c3c 45%, var(--photo-dark) 85%);
    border-radius: 160px 160px 20px 20px;
  }

  .main-nav { position: absolute; left: 0; top: 0; }
  .main-nav a {
    position: absolute; font-family: "Arimo", Arial, sans-serif; font-weight: 700;
    font-size: 11px; line-height: 14px; color: var(--text); text-decoration: none;
    letter-spacing: 0.2px; white-space: nowrap;
  }
  .nav-main { left: 322px; top: 218px; }
  .nav-about { left: 322px; top: 253px; }
  .nav-services { left: 322px; top: 287px; }
  .nav-contact { left: 322px; top: 322px; }

  .role-title {
    position: absolute; left: 249px; top: 488px; white-space: nowrap;
    font-family: "Open Sans", Arial, sans-serif; font-weight: 600; font-size: 20px;
    color: var(--text); letter-spacing: 0.2px;
  }

  .intro-title {
    position: absolute; left: 432px; top: 592px; width: 400px; text-align: center;
    font-family: "Tinos", "Times New Roman", serif; font-weight: 700; font-size: 26px;
    color: var(--text); letter-spacing: 0.6px; line-height: 36px; white-space: nowrap;
  }
  .intro-text {
    position: absolute; left: 337px; top: 626px;
    font-family: "Carlito", Calibri, sans-serif; font-style: italic;
    font-size: 20px; line-height: 27px; color: var(--text-soft);
  }
  .intro-text span { display: block; white-space: nowrap; }
  .learn-more {
    position: absolute; left: 491px; top: 779px; width: 213px; height: 28px;
    font-family: "Open Sans", Arial, sans-serif; font-weight: 700; font-size: 13px;
    color: var(--text); text-decoration: none; text-align: center; line-height: 28px;
    letter-spacing: 0.4px; padding-right: 14px; white-space: nowrap;
  }

  .social { position: absolute; left: 239px; top: 890px; display: flex; gap: 22px; list-style: none; }
  .social li {
    width: 46px; height: 46px; border-radius: 50%; background: var(--icon-grey);
    font-family: "Open Sans", Arial, sans-serif; font-weight: 700; font-size: 13px;
    color: var(--text); display: flex; align-items: center; justify-content: center;
  }
  .phone {
    position: absolute; left: 949px; top: 905px; white-space: nowrap;
    font-family: "Open Sans", Arial, sans-serif; font-weight: 700; font-size: 14px;
    color: var(--text); letter-spacing: 0.3px;
  }
</style>
</head>
<body>
<div class="page">
  <svg class="shapes" width="1200" height="991" viewBox="0 0 1200 991" aria-hidden="true">
    <defs>
      <linearGradient id="panel" x1="0" y1="0" x2="0" y2="1">
        <stop offset="0" stop-color="var(--panel-top)"/>
        <stop offset="1" stop-color="var(--panel-bottom)"/>
      </linearGradient>
      <linearGradient id="band" x1="0" y1="0" x2="1" y2="1">
        <stop offset="0" stop-color="var(--band-blue-dark)"/>
        <stop offset="0.5" stop-color="var(--band-blue)"/>
        <stop offset="1" stop-color="var(--band-blue-light)"/>
      </linearGradient>
    </defs>
    <polygon class="side-panel" points="0,0 317,0 590,570 0,570" fill="url(#panel)"/>
    <polygon class="menu-active" points="183,207 425,207 430,243 200,243" fill="var(--menu-active)"/>
    <line x1="200" y1="243" x2="432" y2="243" stroke="#4a5cc0" stroke-width="1.5"/>
    <line x1="217" y1="277" x2="449" y2="277" stroke="var(--rule)" stroke-width="1"/>
    <line x1="232" y1="311" x2="464" y2="311" stroke="var(--rule)" stroke-width="1"/>
    <line x1="248" y1="345" x2="480" y2="345" stroke="var(--rule)" stroke-width="1"/>
  </svg>

  <div class="portrait" role="img" aria-label="Black and white portrait photo of the accountant, standing with hands clasped"></div>

  <svg class="shapes" width="1200" height="991" viewBox="0 0 1200 991" role="img" aria-label="Blue-tinted photo of office buildings">
    <polygon points="0,568 1200,576 1200,842 712,842 700,836 0,836" fill="url(#band)"/>
    <polygon class="learn-more-shape" points="491,779 690,779 704,807 491,807" fill="var(--accent)"/>
  </svg>

  <nav class="main-nav">
    <a class="nav-main" href="#main">MAIN</a>
    <a class="nav-about" href="#about">ABOUT ME</a>
    <a class="nav-services" href="#services">SERVICES</a>
    <a class="nav-contact" href="#contact">CONTACT ME</a>
  </nav>

  <h1 class="role-title">PROFESSIONAL ACCOUNTANT</h1>

  <h2 class="intro-title">BEST IN CLASS</h2>
  <p class="intro-text">
    <span>Lorem ipsum dolor sit amet, consectetur adipiscing elit, sed do</span>
    <span>eiusmod tempor incididunt ut labore et dolore magna aliqua.</span>
    <span>Ut enim ad minim veniam, quis nostrud exercitation ullamco</span>
    <span>laboris nisi ut aliquip ex ea commodo consequat. Duis aute</span>
    <span>irure dolor in reprehenderit in voluptate.</span>
  </p>
  <a class="learn-more" href="#about">LEARN MORE</a>

  <ul class="social">
    <li aria-label="Vidora">Vi</li>
    <li aria-label="Chirplet">Ch</li>
    <li aria-label="Booklane">Bo</li>
    <li aria-label="Picbox">Pi</li>
  </ul>
  <p class="phone">PHONE : +123-9876543-21</p>
</div>
</body>
</html>
```